Roaming outings business card

please see website
www.roamingoutings.comau

info needed on card
Keiran Voss
Ph
email
Adventure Riding GPS trails

please use my logo and colours off my site

Business

Keiran Voss
keiran@roamingoutings.com

```html
<!DOCTYPE html>
<html lang="en">
<head>
<meta charset="utf-8">
<title>Roaming outings – business card</title>
<link href="https://fonts.googleapis.com/css2?family=Open+Sans:wght@400;600;700;800&display=swap" rel="stylesheet">
<style>
  :root {
    --backdrop: #8e8e8e;
    --yellow-light: #fff04a;
    --yellow-deep: #ffc800;
    --ink: #111111;
    --panel-black: #000000;
    --band-grey: #c9c9c9;
    --paper: #ffffff;
  }
  html, body {
    margin: 0;
    width: 1200px;
    height: 900px;
    overflow: hidden;
    background: var(--backdrop);
    font-family: "Open Sans", Arial, sans-serif;
    color: var(--ink);
  }
  .canvas { position: relative; width: 1200px; height: 900px; }
  .card {
    position: absolute;
    width: 600px;
    height: 340px;
    overflow: hidden;
    box-shadow: 0 10px 24px rgba(0,0,0,.35);
  }
  /* Front card */
  .card--front {
    left: 520px; top: 90px;
    background: linear-gradient(180deg, var(--yellow-light), var(--yellow-deep));
  }
  .brand {
    position: absolute;
    left: 0; right: 0; top: 96px;
    display: flex; align-items: center; justify-content: center; gap: 16px;
  }
  .brand__dot {
    width: 44px; height: 44px; border-radius: 50%;
    background: var(--ink);
  }
  .brand__name {
    font-size: 42px; font-weight: 800; letter-spacing: .5px;
    color: var(--ink);
  }
  .tagline {
    position: absolute; left: 0; right: 0; top: 162px;
    text-align: center; font-size: 17px; font-weight: 700;
  }
  .web-rule {
    position: absolute; left: 0; right: 0; top: 210px;
    display: flex; align-items: center; gap: 14px;
    font-size: 15px; font-weight: 600;
  }
  .web-rule::before, .web-rule::after {
    content: ""; flex: 1; height: 1.5px; background: var(--ink);
  }
  .web-rule::after { margin-top: 22px; }
  .web-rule::before { margin-top: -22px; }

  /* Back card */
  .card--back { left: 80px; top: 470px; }
  .card__bg { position: absolute; inset: 0; }
  .side-name {
    position: absolute; left: 40px; top: 150px;
    display: flex; align-items: center; gap: 10px;
    font-size: 24px; font-weight: 800; color: var(--paper);
  }
  .side-name__dot { width: 22px; height: 22px; border-radius: 50%; background: var(--yellow-deep); }
  .contact {
    position: absolute; right: 36px; top: 150px;
    text-align: right;
  }
  .contact__name { font-size: 24px; font-weight: 700; margin: 0 0 14px; }
  .contact__line {
    display: flex; align-items: center; justify-content: flex-end; gap: 8px;
    font-size: 19px; line-height: 28px; margin: 0;
  }
  .contact__icon { width: 14px; height: 14px; fill: var(--ink); }
</style>
</head>
<body>
<main class="canvas">

  <section class="card card--front">
    <div class="brand">
      <span class="brand__dot"></span>
      <span class="brand__name">Roaming outings</span>
    </div>
    <p class="tagline">Adventure Riding GPS trails</p>
    <div class="web-rule">www.roamingoutings.com</div>
  </section>

  <section class="card card--back">
    <svg class="card__bg" viewBox="0 0 600 340" preserveAspectRatio="none" aria-hidden="true">
      <defs>
        <linearGradient id="backYellow" x1="0" y1="0" x2="0" y2="1">
          <stop offset="0" stop-color="#fff04a"/>
          <stop offset="1" stop-color="#ffc800"/>
        </linearGradient>
      </defs>
      <rect width="600" height="340" fill="url(#backYellow)"/>
      <path d="M0 0 H268 C330 60 330 230 200 340 H0 Z" fill="#c9c9c9"/>
      <path d="M0 0 H252 C310 60 305 230 175 322 C120 334 60 340 0 340 Z" fill="#000"/>
      <path d="M268 0 C330 60 330 230 200 340" fill="none" stroke="#000" stroke-width="2"/>
    </svg>
    <div class="side-name">
      <span class="side-name__dot"></span>
      <span>Roaming outings</span>
    </div>
    <div class="contact">
      <p class="contact__name">Keiran Voss</p>
      <p class="contact__line">044-987 650 321
        <svg class="contact__icon" viewBox="0 0 16 16"><path d="M3 2h3l1 4-2 1a9 9 0 0 0 4 4l1-2 4 1v3c0 1-1 1-2 1A12 12 0 0 1 2 4c0-1 0-2 1-2z"/></svg>
      </p>
      <p class="contact__line">keiran@roamingoutings.com
        <svg class="contact__icon" viewBox="0 0 16 16"><path d="M1 3h14v10H1z M1 3l7 6 7-6" stroke="#fff" stroke-width="1"/></svg>
      </p>
      <p class="contact__line">www.roamingoutings.comau
        <svg class="contact__icon" viewBox="0 0 16 16"><path d="M6 10l4-4M5 8l-2 2a2 2 0 0 0 3 3l2-2M11 8l2-2a2 2 0 0 0-3-3L8 5" fill="none" stroke="#111" stroke-width="1.8"/></svg>
      </p>
    </div>
  </section>

</main>
</body>
</html>
```